Roofing Contractor business card redesign

I want to redesign my business card with a fresh, eye catching concept

Target Market(s)

Residential Roofing Clients, potential employees, and subcontractors.

Industry/Entity Type

Business

Colors

Designer to choose colors to be used in the design.

Requirements
Nice to have
• I just want something that's more pleasing to the eye. You can use a combination of either / or of my logos.

```html
<!DOCTYPE html>
<html lang="en">
<head>
<meta charset="utf-8">
<title>Fair Hand Builders – Business Cards</title>
<link href="https://fonts.googleapis.com/css2?family=Lato:wght@400;700;900&display=swap" rel="stylesheet">
<style>
  :root {
    --bg: #3a3a3a;
    --orange: #e8782a;
    --brown: #4a1b14;
    --brown-band: #6e3a1c;
    --ink: #3b3b3b;
    --paper: #ffffff;
    --paper-soft: #ececec;
  }
  * { margin: 0; padding: 0; box-sizing: border-box; }
  html, body { width: 1200px; height: 900px; overflow: hidden; }
  body {
    background: var(--bg);
    font-family: "Lato", sans-serif;
    position: relative;
  }
  .card {
    position: absolute;
    width: 560px;
    height: 320px;
    border-radius: 18px;
    overflow: hidden;
    box-shadow: 0 10px 30px rgba(0,0,0,0.45);
  }
  /* ---------- front ---------- */
  .card-front { left: 70px; top: 90px; background: var(--paper); }
  .front-art {
    position: absolute; left: 170px; top: 20px;
    width: 250px; height: 250px; border-radius: 50%;
    background: radial-gradient(circle, rgba(0,0,0,0.06), rgba(0,0,0,0.03));
  }
  .front-logo {
    position: absolute; left: 0; right: 0; top: 92px;
    display: flex; align-items: center; justify-content: center; gap: 14px;
  }
  .logo-dot {
    width: 44px; height: 44px; border-radius: 50%;
    background: var(--orange); flex: none;
  }
  .logo-name {
    font-weight: 900; color: var(--brown);
    font-size: 34px; letter-spacing: 0.5px; white-space: nowrap;
  }
  .front-band {
    position: absolute; left: 0; right: 0; top: 190px; height: 36px;
    background: var(--orange);
    display: flex; align-items: center; justify-content: center;
    color: #fff; font-size: 15px; letter-spacing: 0.5px;
  }
  .front-stripe {
    position: absolute; left: 0; right: 0; top: 262px; height: 18px;
    background: var(--orange);
  }
  /* ---------- back ---------- */
  .card-back { left: 570px; top: 480px; background: var(--paper-soft); }
  .back-shapes { position: absolute; inset: 0; }
  .back-art {
    position: absolute; left: 14px; top: 10px;
    width: 190px; height: 160px; border-radius: 50%;
    background: radial-gradient(circle, rgba(255,255,255,0.16), rgba(255,255,255,0.05));
  }
  .back-logo {
    position: absolute; left: 16px; top: 168px;
    display: flex; align-items: center; gap: 8px;
  }
  .back-logo .logo-dot { width: 24px; height: 24px; background: var(--paper); }
  .back-logo .logo-name { font-size: 17px; letter-spacing: 0.2px; }
  .back-web {
    position: absolute; left: 0; top: 222px; width: 250px; height: 36px;
    display: flex; align-items: center; justify-content: center;
    color: #fff; font-size: 13px; letter-spacing: 0.4px;
  }
  .contact {
    position: absolute; right: 26px; top: 24px; text-align: right;
  }
  .contact-name { font-size: 27px; color: var(--ink); font-weight: 400; }
  .contact-role { color: var(--orange); font-size: 12.5px; line-height: 1.35; margin-top: 2px; }
  .contact-list { list-style: none; margin-top: 12px; font-size: 14px; color: var(--ink); }
  .contact-list li {
    display: flex; align-items: center; justify-content: flex-end; gap: 8px;
    line-height: 1.5;
  }
  .contact-list svg { width: 13px; height: 13px; flex: none; fill: var(--orange); }
  .address { line-height: 1.3; margin-top: 2px; }
  .social-bar {
    position: absolute; right: 0; top: 256px; width: 270px; height: 34px;
    display: flex; align-items: center; justify-content: flex-end; gap: 6px;
    padding-right: 26px; color: #fff; font-size: 14px;
  }
  .social-chip { width: 13px; height: 13px; background: var(--orange); border-radius: 2px; }
</style>
</head>
<body>

  <section class="card card-front" aria-label="Card front">
    <div class="front-art" role="img" aria-label="Faint illustration of a team of builders"></div>
    <div class="front-logo">
      <span class="logo-dot"></span>
      <span class="logo-name">Fair Hand Builders, Inc.</span>
    </div>
    <div class="front-band">www.fairhandtx.com</div>
    <div class="front-stripe"></div>
  </section>

  <section class="card card-back" aria-label="Card back">
    <svg class="back-shapes" width="560" height="320" viewBox="0 0 560 320">
      <polygon points="0,0 188,0 300,320 0,320" fill="var(--orange)"/>
      <polygon points="200,0 224,0 300,256 276,256" fill="var(--brown)"/>
      <polygon points="0,222 266,222 278,258 0,258" fill="var(--brown-band)"/>
      <polygon points="276,256 560,256 560,290 288,290" fill="var(--brown)"/>
    </svg>
    <div class="back-art" role="img" aria-label="Faint illustration of a team of builders"></div>
    <div class="back-logo">
      <span class="logo-dot"></span>
      <span class="logo-name">Fair Hand Builders, Inc.</span>
    </div>
    <div class="back-web">www.fairhandtx.com</div>

    <div class="contact">
      <h1 class="contact-name">Sam Whitlow</h1>
      <p class="contact-role">Keller Certified Roof Inspector<br>Licensed Property Adjuster</p>
      <ul class="contact-list">
        <li>(555) 014-2200
          <svg viewBox="0 0 16 16"><path d="M2 6c0-2 2-3 6-3s6 1 6 3v1h-3V6H5v1H2zM4 8h8l2 5H2z"/></svg></li>
        <li>(555) 017-3381
          <svg viewBox="0 0 16 16"><path d="M4 1h8v14H4zM5.5 2.5v9h5v-9z"/></svg></li>
        <li>sam@fairhandtx.com
          <svg viewBox="0 0 16 16"><path d="M1 3h14v10H1zM2 4l6 5 6-5z"/></svg></li>
        <li class="address">4810 Alder Creek Road Suite 210<br>Riverton, TX 75010
          <svg viewBox="0 0 16 16"><path d="M8 1a5 5 0 0 1 5 5c0 4-5 9-5 9S3 10 3 6a5 5 0 0 1 5-5zm0 3a2 2 0 1 0 0 4 2 2 0 0 0 0-4z"/></svg></li>
      </ul>
    </div>

    <div class="social-bar">
      <span class="social-chip"></span>
      <span>/fairhandbuilders</span>
    </div>
  </section>

</body>
</html>
```